Brochure Design Project

PLEASE USE THE ATTACHED WORD DOC ONLY AS A GUIDE- I WANT TO SEE A TRUE DESIGN AND NOT JUST A RECREATE OF MY CONTENT.

We need a brochure that is geared towards a service mentality. less tech/bold and something very approachable.

we will look for a design concept and then finalize the content laters.

Target Market(s)

nurses and business owners

Industry/Entity Type

Tech

```html
<!DOCTYPE html>
<html lang="en">
<head>
<meta charset="utf-8">
<title>Seacrest Pharmacy Trifold Brochure</title>
<link rel="stylesheet" href="https://fonts.googleapis.com/css2?family=Roboto:wght@300;400;500&display=swap">
<style>
:root{
  --purple:#6b1a66;
  --blue:#5cade2;
  --blue-light:#8cc6ec;
  --ink:#333;
  --paper:#fff;
  --stage:#e9e9ea;
}
*{margin:0;padding:0;box-sizing:border-box}
html,body{width:1200px;height:900px;overflow:hidden;background:var(--stage)}
body{font-family:"Roboto",Arial,sans-serif;color:var(--ink);position:relative}
.sheet{position:absolute;width:540px;height:420px;background:var(--paper);box-shadow:0 1px 3px rgba(0,0,0,.18)}
.sheet--outside{left:50px;top:30px}
.sheet--inside{left:610px;top:450px}
.panel{position:absolute;top:0;width:180px;height:420px;overflow:hidden}
.panel+.panel{border-left:1px solid #e4e4e4}
.panel--1{left:0}.panel--2{left:180px}.panel--3{left:360px}
.panel__art{position:absolute;inset:0;width:100%;height:100%}
.abs{position:absolute}
.title{font-weight:300;text-transform:uppercase;line-height:.95;white-space:nowrap}
.body{font-size:6.2px;line-height:1.45;color:var(--ink)}
.bullets{list-style:none}
.bullets li{position:relative;padding-left:9px;margin-bottom:3px}
.bullets li::before{content:"";position:absolute;left:1px;top:2.6px;width:2.4px;height:2.4px;border-radius:50%;background:currentColor}
.brand{background:var(--paper);display:flex;flex-direction:column;align-items:center;justify-content:center;gap:3px}
.brand__mark{width:8px;height:8px;background:var(--blue)}
.brand__name{font-size:8px;font-weight:400;color:var(--purple);letter-spacing:.2px}
.contact{font-size:5.4px;line-height:1.5;color:#fff}
.tag{display:inline-block;font-size:6px;font-weight:500;padding:2px 10px 2px 5px;margin-bottom:4px;clip-path:polygon(0 0,100% 0,calc(100% - 6px) 100%,0 100%)}
.tag--light{background:#fff;color:var(--ink)}
.tag--dark{background:var(--purple);color:#fff}
.service-item{margin-bottom:8px}
.benefit-item{margin-bottom:9px}
</style>
</head>
<body>

<section class="sheet sheet--outside">
  <div class="panel panel--1">
    <svg class="panel__art" viewBox="0 0 180 420" preserveAspectRatio="none" aria-hidden="true">
      <path d="M0 0H180V28C120 34 60 50 0 70Z" fill="var(--purple)"/>
      <path d="M0 70C60 50 120 34 180 28V80C120 95 60 108 0 110Z" fill="var(--blue)"/>
    </svg>
    <h2 class="title abs" style="left:12px;top:82px;font-size:19px;color:#fff">Hospice</h2>
    <h3 class="title abs" style="left:12px;top:113px;font-size:11px;color:var(--purple)">Care Network</h3>
    <ul class="bullets body abs" style="left:12px;top:138px;width:160px">
      <li>Reduce Medication Costs</li>
      <li>Clinical Pharmacist reviews drug use and provides customized reports</li>
      <li>Improve Formularies and formulary management</li>
      <li>Fill prescriptions at thousands at any of our Hospice Care Network pharmacies nationwide</li>
      <li>24/7 Service</li>
    </ul>
    <p class="body abs" style="left:12px;top:216px;width:160px">Seacrest Pharmacy Hospice Care Network (HCN) allows hospices access to lower medication costs and formulary control with our clinical formulary experts. HCN also provides the convenience for families and caregivers to have access to a full palliative medication inventory, including customized comfort kits and hospice-specific compounds, all of which are delivered directly to the patient's site of care. Seacrest's HCN boasts an extensive palliative care medication formulary and pharmacy network, which ensures access to the medications most needed by hospice patients anytime and anywhere.</p>
  </div>

  <div class="panel panel--2">
    <svg class="panel__art" viewBox="0 0 180 420" preserveAspectRatio="none" aria-hidden="true">
      <rect x="12" y="12" width="156" height="396" fill="var(--blue)"/>
      <path d="M12 12H168V70C120 90 60 80 12 100Z" fill="var(--purple)"/>
      <path d="M12 100C60 80 120 90 168 70V180C110 200 60 230 12 260Z" fill="var(--blue-light)" opacity=".55"/>
    </svg>
    <div class="brand abs" style="left:20px;top:330px;width:40px;height:40px">
      <span class="brand__mark"></span>
      <span class="brand__name" style="font-size:6px">seacrest</span>
    </div>
    <p class="contact abs" style="left:66px;top:332px;width:100px">2040 Harbor Way Suite 18<br>Bayview, CA 90000<br>Phone: (555) 010-4170<br>Fax: (555) 010-4171<br>After Hours On Call: (555) 010-0750</p>
  </div>

  <div class="panel panel--3">
    <svg class="panel__art" viewBox="0 0 180 420" preserveAspectRatio="none" aria-hidden="true">
      <path d="M0 0H180V100C120 110 60 130 0 150Z" fill="var(--purple)"/>
      <path d="M0 150C60 130 120 110 180 100V150C120 160 60 180 0 200Z" fill="var(--blue)"/>
    </svg>
    <div class="brand abs" style="left:10px;top:0;width:46px;height:70px">
      <span class="brand__mark"></span>
      <span class="brand__name">seacrest</span>
    </div>
    <h1 class="title abs" style="left:10px;top:112px;font-size:21px;color:#fff">Big City<br>Support</h1>
    <p class="title abs" style="left:10px;top:156px;font-size:16px;color:var(--purple)">Small Town</p>
    <p class="title abs" style="left:10px;top:172px;font-size:25px;color:var(--purple)">Service</p>
    <p class="abs" style="left:10px;top:214px;font-size:7px;line-height:1.35;text-transform:uppercase">Hospice<br>Long Term Care<br>Skilled Nursing</p>
    <p class="abs" style="left:10px;top:296px;font-size:8px;line-height:1.3;color:var(--purple);text-transform:uppercase">Experts in<br><strong style="font-weight:500">Customized Health Care</strong></p>
  </div>
</section>

<section class="sheet sheet--inside">
  <div class="panel panel--1">
    <svg class="panel__art" viewBox="0 0 180 420" preserveAspectRatio="none" aria-hidden="true">
      <path d="M0 155C60 135 120 125 180 128V420H0Z" fill="var(--blue)"/>
      <path d="M0 355C60 370 120 330 180 300V420H0Z" fill="var(--purple)"/>
    </svg>
    <h2 class="abs" style="left:12px;top:24px;width:160px;font-size:11.5px;font-weight:300;line-height:1.1;text-transform:uppercase;color:var(--purple)">By compounding medications, we can improve patient outcomes and simplify medication administration caregivers</h2>
    <ul class="bullets body abs" style="left:12px;top:180px;width:155px;color:#fff">
      <li>Customized Combinations simplify medication administration</li>
      <li>Dosage form Changes</li>
      <li>Transdermal Pain Management for site specific therapy</li>
      <li>Sugar-Free therapy for diabetic patients</li>
      <li>Lactose Capsules</li>
      <li>Customized dosage for kidney or liver failure patients</li>
    </ul>
  </div>

  <div class="panel panel--2">
    <svg class="panel__art" viewBox="0 0 180 420" preserveAspectRatio="none" aria-hidden="true">
      <rect x="0" y="0" width="180" height="420" fill="var(--blue)"/>
      <path d="M0 0H180V22C120 30 60 20 0 32Z" fill="var(--purple)"/>
      <path d="M0 410C60 404 120 412 180 402V420H0Z" fill="var(--purple)"/>
    </svg>
    <div class="abs" style="left:10px;top:44px;width:160px">
      <div class="service-item"><span class="tag tag--light">Service:</span><p class="body" style="color:#fff">Our service sets us apart from retail pharmacies as well as large impersonal pharmacies. As your pharmacy partner, you'll have access to our pharmacy owners knowledge staff to address concerns, find solutions, and ultimately provide better care while increasing your profitability.</p></div>
      <div class="service-item"><span class="tag tag--light">Timely Deliveries</span><p class="body" style="color:#fff">When it comes to timely deliveries, Seacrest has multiple solutions to get you the medications you need quickly. With our pharmacy network, we can deliver medications at anytime, for any reason.</p></div>
      <div class="service-item"><span class="tag tag--light">MAR or EMAR</span><p class="body" style="color:#fff">We support EMAR or provide paper MARs if desired. Our goal is to work with your current system, not against it.</p></div>
      <div class="service-item"><span class="tag tag--light">Customized Formularies</span><p class="body" style="color:#fff">We help you manage healthcare costs and limit staff dispensing time by creating formularies that focus on generic and customized compounded medications.</p></div>
      <div class="service-item"><span class="tag tag--light">Technology Solutions</span><p class="body" style="color:#fff">Seacrest provides great time saving technology solutions that you won't find with other local small pharmacies. We are constantly offer new and exciting ways to reduce staff time and increase profitability.</p></div>
    </div>
  </div>

  <div class="panel panel--3">
    <svg class="panel__art" viewBox="0 0 180 420" preserveAspectRatio="none" aria-hidden="true">
      <path d="M0 300C60 330 120 310 180 280V420H0Z" fill="var(--blue)"/>
      <path d="M0 318C60 345 120 330 180 300V420H0Z" fill="var(--purple)"/>
    </svg>
    <div class="abs" style="left:10px;top:18px;width:162px">
      <div class="benefit-item"><span class="tag tag--dark">Medicare Part D Partners</span><p class="body">We handle therapeutic interchange, prior authorizations, and physician global authorizations so you don't have to.</p></div>
      <div class="benefit-item"><span class="tag tag--dark">Medicare Part A</span><p class="body">Utilizing our pharmacy network, we minimize billing issues with price transparency and accuracy. This allows us focus on corporate strategies to manage your pharmacy expenses. Monthly reports helps identify trends, non-formulary utilization and clinical standards to ensure your facility is saving time and money.</p></div>
      <div class="benefit-item"><span class="tag tag--dark">Consultant Pharmacists</span><p class="body">Our pharmacists provide regulatory compliance assistance to minimize your risk and reduce issues during facility surveys.</p></div>
      <div class="benefit-item"><span class="tag tag--dark">Continuing Education</span><p class="body">CE for caretakers leads to better outcomes for your residents and your bottom line.</p></div>
    </div>
  </div>
</section>

</body>
</html>
```